Updated Business Card Re-design (Logo Provided)

I am needing to update our business cards for our practice, Bright Harbor Care. We are a personal injury and wellness practice. The final design should be elegant and classy, but a type of card people would want to keep. Any samples should only have Dr. Tarek Minouvel on the template.
Updates

Went on vacation/holiday

Need extra days to review

Target Market(s)

Personal Injury clients, wellness clients

Industry/Entity Type

Personal Injury, medical, wellness

Contact Information for Business Card

dr and practice name, offerings

Requirements
Must have
• Single sided, this will be printed on a transparent business card, no exceptions.

```html
<!DOCTYPE html>
<html lang="en">
<head>
<meta charset="UTF-8">
<title>Bright Harbor Care – Business Card</title>
<link href="https://fonts.googleapis.com/css2?family=Montserrat:wght@400;500;700&display=swap" rel="stylesheet">
<style>
  :root {
    --page-bg: #ffffff;
    --card-bg: #ffffff;
    --card-border: #8a8a8a;
    --table-line: #5a5a5a;
    --brand-blue: #3f6db3;
    --brand-green: #4f8a4a;
    --brand-orange: #e0902f;
    --name-ink: #464646;
  }
  * { margin: 0; padding: 0; box-sizing: border-box; }
  html, body {
    width: 1173px;
    height: 1200px;
    overflow: hidden;
    background: var(--page-bg);
    font-family: "Montserrat", sans-serif;
  }
  .business-card {
    position: absolute;
    left: 86px;
    top: 277px;
    width: 1000px;
    height: 646px;
    background: var(--card-bg);
    border: 1px solid var(--card-border);
  }
  .brand {
    position: absolute;
    left: 96px;
    top: 66px;
    display: flex;
    align-items: center;
    gap: 18px;
  }
  .brand-dot {
    width: 54px;
    height: 54px;
    border-radius: 50%;
    background: var(--brand-orange);
  }
  .brand-name {
    color: var(--brand-blue);
    font-weight: 700;
    font-size: 31px;
    line-height: 34px;
    text-align: center;
    text-transform: uppercase;
  }
  .doctor {
    position: absolute;
    left: 0;
    width: 1044px;
    top: 232px;
    text-align: center;
  }
  .doctor-name {
    color: var(--name-ink);
    font-weight: 700;
    font-size: 55px;
    line-height: 64px;
    text-transform: uppercase;
    letter-spacing: -0.5px;
  }
  .doctor-rule {
    width: 486px;
    height: 3px;
    margin: 6px auto 0;
    background: var(--brand-green);
  }
  .doctor-tagline {
    color: var(--brand-green);
    font-weight: 500;
    font-size: 36px;
    letter-spacing: 3px;
    margin-top: 8px;
  }
  .services {
    position: absolute;
    left: 141px;
    top: 425px;
    width: 762px;
    border-collapse: collapse;
    table-layout: fixed;
  }
  .services td {
    height: 79px;
    border: 1.5px solid var(--table-line);
    color: var(--brand-blue);
    font-size: 33px;
    font-weight: 400;
    text-align: center;
    vertical-align: middle;
  }
</style>
</head>
<body>
  <article class="business-card">
    <header class="brand">
      <span class="brand-dot"></span>
      <span class="brand-name">Bright Harbor<br>Care</span>
    </header>

    <section class="doctor">
      <h1 class="doctor-name">Dr. Tarek Minouvel</h1>
      <div class="doctor-rule"></div>
      <p class="doctor-tagline">Integrated Medical Care</p>
    </section>

    <table class="services">
      <tr>
        <td>Personal Injury</td>
        <td>Pain Management</td>
      </tr>
      <tr>
        <td>Wellness</td>
        <td>Ortho Services</td>
      </tr>
    </table>
  </article>
</body>
</html>
```